Business Card Design for Varnok Facility Services

We are looking for a Business Card Design for the Company "Varnok Facility Services."
Front side:
- Company Logo (small)
- Company Name, address, pohone, website and personal data.
- white background, for text e.g. company colors (blue or green like in the logo)
Please use following data:
Company data:
Varnok Facility Services Tulbrecht
Kirchmattweg 12
6331 Cham
www.varnok-fs.ch
Person data:
Ruben Tulbrecht
Geschäftsführer
+41 76 519 84 60
info@varnok-fs.ch
Back side:
could be colored in blue or green
please use a big logo sing and some smaller icons to say what is all beeing offered in facility services, like cleaning, maintenance cleaning
industrial cleaning, caretaking, gardening, disposal. There is no need for everyone of the icons if there are similar or an icon is standing for more of them.
Cleaning Service
colors to use:
blue: HEX 246BB0
green: HEX 52B33E

```html
<!DOCTYPE html>
<html lang="de">
<head>
<meta charset="utf-8">
<title>Varnok Facility Services – Visitenkarte</title>
<link href="https://fonts.googleapis.com/css2?family=Jost:ital,wght@0,300;0,400;0,500;0,700;1,400&display=swap" rel="stylesheet">
<style>
  :root {
    --blue: #246BB0;
    --green: #52B33E;
    --dark: #323232;
    --icon-dark: #2b2b2b;
    --paper: #ffffff;
    --back-top: #4aa66a;
    --back-bottom: #2b7f9b;
  }
  * { margin: 0; padding: 0; box-sizing: border-box; }
  html, body { width: 1200px; height: 1200px; overflow: hidden; background: var(--paper); }
  body { position: relative; font-family: "Jost", sans-serif; }

  .card {
    position: absolute;
    left: 109px;
    width: 986px;
    height: 563px;
    overflow: hidden;
    box-shadow: 6px 6px 8px rgba(0,0,0,0.45);
  }
  .card--front { top: 25px; background: var(--paper); }
  .card--back {
    top: 614px;
    background: linear-gradient(180deg, var(--back-top) 0%, var(--back-bottom) 100%);
  }

  .front-curve { position: absolute; inset: 0; width: 986px; height: 563px; }

  .company-line {
    position: absolute; left: 50px; top: 42px;
    font-style: italic; font-weight: 400; font-size: 30px;
    color: var(--green); white-space: nowrap;
  }
  .person {
    position: absolute; right: 56px; top: 40px; text-align: right;
  }
  .person__name {
    font-size: 58px; line-height: 1; color: var(--blue); white-space: nowrap;
  }
  .person__first { font-weight: 300; }
  .person__last { font-weight: 500; }
  .person__role {
    font-size: 30px; font-weight: 700; color: var(--green); line-height: 1.1;
  }

  .contact-list { position: absolute; left: 533px; top: 204px; list-style: none; }
  .contact-item {
    display: flex; align-items: center; height: 80px;
  }
  .contact-icon {
    width: 62px; height: 62px; border-radius: 50%;
    background: var(--icon-dark); flex: none;
    display: flex; align-items: center; justify-content: center;
  }
  .contact-text {
    margin-left: 10px; font-size: 25px; color: var(--green);
    line-height: 1.2; letter-spacing: 0.5px;
  }

  .brand-small {
    position: absolute; left: 48px; top: 415px;
    display: flex; align-items: center; gap: 14px;
  }
  .brand-small__dot { width: 34px; height: 34px; border-radius: 50%; background: var(--green); }
  .brand-small__name {
    font-weight: 500; font-size: 30px; line-height: 1.1; color: var(--green);
  }

  .brand-large {
    position: absolute; left: 0; right: 0; top: 170px;
    display: flex; flex-direction: column; align-items: center; gap: 26px;
  }
  .brand-large__dot { width: 90px; height: 90px; border-radius: 50%; background: var(--blue); }
  .brand-large__name {
    font-weight: 500; font-size: 56px; letter-spacing: 3px; color: var(--blue);
    text-align: center; line-height: 1.05;
  }

  .service-icon {
    position: absolute; top: 451px; width: 66px; height: 66px;
    border-radius: 50%; background: var(--paper);
  }
  .service-icon--cleaning { left: 178px; }
  .service-icon--spray { left: 453px; }
  .service-icon--disposal { left: 741px; }
</style>
</head>
<body>

<section class="card card--front" aria-label="Vorderseite">
  <svg class="front-curve" viewBox="0 0 986 563" aria-hidden="true">
    <path d="M0,0 C70,260 300,500 640,563 L0,563 Z" fill="#111"/>
    <path d="M0,8 C80,270 300,505 620,563 L0,563 Z" fill="var(--dark)"/>
  </svg>

  <p class="company-line">Varnok Facility Services Tulbrecht</p>

  <div class="person">
    <h1 class="person__name"><span class="person__first">Ruben</span> <span class="person__last">Tulbrecht</span></h1>
    <p class="person__role">Geschäftsführer</p>
  </div>

  <ul class="contact-list">
    <li class="contact-item">
      <span class="contact-icon">
        <svg width="40" height="40" viewBox="0 0 40 40" fill="none" stroke="#fff" stroke-width="3">
          <circle cx="20" cy="20" r="16"/>
          <ellipse cx="20" cy="20" rx="7" ry="16"/>
          <line x1="4" y1="20" x2="36" y2="20"/>
          <line x1="7" y1="12" x2="33" y2="12"/>
          <line x1="7" y1="28" x2="33" y2="28"/>
        </svg>
      </span>
      <span class="contact-text">www.varnok-fs.ch</span>
    </li>
    <li class="contact-item">
      <span class="contact-icon">
        <svg width="30" height="40" viewBox="0 0 30 40">
          <path d="M15 2C7.5 2 2 7.5 2 14.5 2 24 15 38 15 38S28 24 28 14.5C28 7.5 22.5 2 15 2Z" fill="#fff"/>
          <circle cx="15" cy="14" r="5" fill="var(--icon-dark)"/>
        </svg>
      </span>
      <span class="contact-text">Kirchmattweg 12<br>6331 Cham</span>
    </li>
    <li class="contact-item">
      <span class="contact-icon">
        <svg width="36" height="36" viewBox="0 0 36 36">
          <path d="M8 3 L13 3 L15 11 L11 14 C13 19 17 23 22 25 L25 21 L33 23 L33 28 C33 31 30 33 27 33 C14 31 5 22 3 9 C3 6 5 3 8 3Z" fill="#fff"/>
        </svg>
      </span>
      <span class="contact-text">+41 76 519 84 60</span>
    </li>
    <li class="contact-item">
      <span class="contact-icon">
        <svg width="40" height="28" viewBox="0 0 40 28" fill="none" stroke="#fff" stroke-width="2.5">
          <rect x="2" y="2" width="36" height="24" fill="#fff" stroke="none"/>
          <path d="M2 2 L20 16 L38 2" stroke="var(--icon-dark)"/>
          <path d="M2 26 L15 12 M38 26 L25 12" stroke="var(--icon-dark)"/>
        </svg>
      </span>
      <span class="contact-text">info@varnok-fs.ch</span>
    </li>
  </ul>

  <div class="brand-small">
    <span class="brand-small__dot"></span>
    <span class="brand-small__name">Varnok<br>Facility Services</span>
  </div>
</section>

<section class="card card--back" aria-label="Rückseite">
  <div class="brand-large">
    <span class="brand-large__dot"></span>
    <p class="brand-large__name">VARNOK<br>FACILITY SERVICES</p>
  </div>

  <span class="service-icon service-icon--cleaning" role="img" aria-label="Symbol Reinigung: Bodenwischer"></span>
  <span class="service-icon service-icon--spray" role="img" aria-label="Symbol Unterhaltsreinigung: Sprühflasche"></span>
  <span class="service-icon service-icon--disposal" role="img" aria-label="Symbol Entsorgung: Abfall in Behälter"></span>
</section>

</body>
</html>
```